Corvel Imaging Center web design and code

We need a new website for a Diagnostic Imaging Center in Fort Lauderdale, Florida.
The center has new KW advanced diagnostic equipment including a 3.0 Tesla MRI, a 128 slice PET/CT and a Vantro T4 Ultrasound. Our facility has just been renovated and we have a lot of images, both facility and modality to use.
We have two client types, doctors who send their patients to our clinical Corvel Center division, and clients who self-refer for screening studies to our Tralimo division. Both logos are attached. Please use the colors in the logos for the layout. Site should be coded in conventional HTML with CSS, but support multiple devices.
Updates

Project Deadline Extended
Reason: Waiting for additional designs. Most of the current designs are very similar in their structure and we would like more variety in terms of layout.

Target Market(s)

Doctors who refer patients for MRI, CT, PET, Bone Density and Ultrasound scans,
and
Retail clients who want full-body screening using MRI.

Industry/Entity Type

Medical Imaging

Coding

Coded - Design and coding required

Number of Pages Required

5+ page

Font styles to use
Sans Serif
Other font styles liked:
• Arquitecta

Requirements
Must have
• A good balance between color, shape, message and people/machine images.
• Must have images of the various machines, (KW Orvanta QX420, KW Orvanta 480, KW Vantro T4) happy patients, clinical people, facility images and information about scans, preparations, costs, insurances we take.
• Must have links for social media and dynamic imagery.
Nice to have
• Some interactivity would be nice, including contact forms and scheduling application, Location map, directions, downloadable forms, history.
Should not have
• We do not want this to be built on WordPress platform. Should not be bound to a database platform that is proprietary or difficult to move.

```html
<!DOCTYPE html>
<html lang="en">
<head>
<meta charset="utf-8">
<title>Corvel Imaging Center</title>
<link href="https://fonts.googleapis.com/css2?family=Open+Sans:wght@400;600;700&display=swap" rel="stylesheet">
<style>
:root{
  --green:#8cc63f;
  --green-dark:#6aa52a;
  --green-soft:#d9eec0;
  --green-pale:#eef7e3;
  --ink:#2d2d2d;
  --text:#666;
  --line:#dcdcdc;
  --white:#fff;
  --photo-skin:#e8ddd3;
  --photo-cool:#dfe6ec;
}
*{box-sizing:border-box;margin:0;padding:0}
html,body{width:1200px;height:2600px;overflow:hidden}
body{font-family:"Open Sans",Arial,sans-serif;color:var(--text);background:var(--white);position:relative;font-size:12px;line-height:1.5}
.abs{position:absolute}
.photo{position:absolute;background:linear-gradient(160deg,var(--photo-cool),var(--photo-skin))}
h2,h3{color:var(--ink);font-weight:700}
.green{color:var(--green)}
.btn{display:inline-block;background:var(--green);color:#fff;font-size:11px;font-weight:600;padding:4px 14px;border-radius:2px}

/* header */
.site-header{top:0;left:0;width:1200px;height:56px;background:#fff;border-bottom:1px solid var(--line)}
.brand{left:240px;top:10px;display:flex;align-items:center;gap:10px}
.brand-dot{width:34px;height:34px;border-radius:50%;background:var(--green)}
.brand-name{font-size:20px;font-weight:700;color:var(--ink);line-height:1.05;width:150px}
.top-contact{right:140px;top:4px;font-size:10px;color:#888}
.main-nav{right:140px;top:22px;display:flex;gap:4px}
.main-nav span{background:var(--green);color:#fff;font-size:9px;font-weight:600;padding:4px 9px}
.main-nav span:first-child{background:var(--ink)}

/* hero */
.hero{top:56px;left:0;width:1200px;height:470px;background:linear-gradient(180deg,var(--green-pale),#fff 85%);overflow:hidden}
.hero-ring{left:356px;top:18px;width:380px;height:380px;border-radius:50%;border:14px solid var(--green-soft)}
.hero-photo{left:376px;top:38px;width:340px;height:340px;border-radius:50%}
.hero-badge{left:640px;top:160px;width:270px;height:270px;border-radius:50%;background:#2f2f2f;border:8px solid var(--green);padding:60px 40px;color:#ccc}
.hero-badge h1{color:var(--green);font-size:24px;line-height:1.15;font-weight:600;margin-bottom:8px}
.hero-badge p{font-size:10px;margin-bottom:10px}

/* intro */
.intro{top:560px;left:0;width:1200px;height:560px}
.section-title{display:flex;align-items:center;gap:8px;font-size:20px;color:var(--ink);font-weight:700}
.section-title i{width:18px;height:18px;border-radius:50%;background:var(--green);display:inline-block}
.intro p{font-size:11px}
.callout h3{color:var(--green);font-size:16px;line-height:1.2;margin-bottom:6px}
.schedule-box{left:720px;top:120px;width:340px;height:280px;background:var(--green-pale);border:1px solid var(--green-soft)}
.schedule-box .bar{background:var(--ink);color:#fff;font-size:11px;font-weight:600;padding:8px 12px}
.schedule-box .phone{color:var(--green);font-size:18px;font-weight:700;padding:8px 12px 0}
.schedule-box p{padding:4px 12px}
.field-row{display:flex;gap:8px;padding:6px 12px}
.field-row b{background:var(--ink);color:#fff;font-size:9px;padding:4px 8px}
.highlights{left:240px;top:290px;width:460px}
.highlights h4{color:var(--green);font-size:12px;margin-bottom:4px}
.highlights ul{list-style:none;columns:2;font-size:10px}
.highlights li::before{content:"✓ ";color:var(--green)}

/* blog */
.blog{top:1110px;left:0;width:1200px;height:580px;background:linear-gradient(180deg,var(--green-soft),var(--green-pale))}
.blog-title{top:14px;width:1200px;text-align:center;font-size:24px;color:var(--ink);font-weight:600}
.blog-title b{color:var(--green)}
.card{position:absolute;width:400px;height:220px;background:#fff;border:1px solid var(--line);box-shadow:0 2px 6px rgba(0,0,0,.08)}
.card .thumb{left:12px;top:12px;width:180px;height:196px}
.card .body{position:absolute;left:204px;top:12px;width:184px}
.card h3{font-size:12px;color:var(--green);margin-bottom:4px}
.card p{font-size:10px;line-height:1.45}
.card .btn{position:absolute;right:12px;bottom:12px}

/* team */
.team{top:1720px;left:0;width:1200px;height:320px}
.team-title{width:1200px;text-align:center;font-size:24px;color:var(--ink);font-weight:600}
.team-title b{color:var(--green)}
.team-sub{top:36px;width:1200px;text-align:center;font-size:10px}
.member{position:absolute;top:64px;width:180px;height:240px;border:1px solid var(--line);background:#fff}
.member .photo{left:8px;top:8px;width:162px;height:190px}
.member .name{position:absolute;left:0;bottom:0;width:100%;height:34px;background:var(--green);color:#fff;text-align:center;font-size:11px;font-weight:600;line-height:1.3;padding-top:3px}

/* contact */
.contact{top:2060px;left:0;width:1200px;height:420px}
.contact-info{left:440px;top:0;width:150px}
.contact-info h2{font-size:18px;color:var(--green);font-weight:600;margin-bottom:6px}
.contact-info p{font-size:10px;margin-bottom:6px}
.social{left:240px;top:250px;width:200px;height:70px;background:var(--ink);color:#fff;padding:14px;display:flex;gap:8px;align-items:center}
.social i{width:22px;height:22px;border-radius:50%;background:var(--green);display:inline-block}
.social span{font-size:11px;font-weight:700;line-height:1.1}
.questions{left:610px;top:0;width:440px}
.questions h2{font-size:12px;color:var(--green);font-weight:600;line-height:1}
.questions h2 b{display:block;font-size:22px;color:var(--ink)}
.form{display:grid;grid-template-columns:1fr 1fr;gap:8px;margin-top:12px}
.form label{font-size:10px;display:block}
.form .in{height:24px;border:1px solid var(--line);background:#fff}
.form .msg{height:100px}
.help{left:610px;top:330px;width:440px;height:70px;background:var(--green);color:#fff;padding:12px 16px}
.help strong{font-size:16px;display:block}
.help span{font-size:10px}

/* footer */
.site-footer{top:2490px;left:0;width:1200px;height:110px;background:#2a2a2a;color:#aaa;font-size:10px}
.footer-links{left:240px;top:24px;display:flex;gap:22px;color:#ddd}
.copy{left:240px;top:60px}
</style>
</head>
<body>

<header class="site-header abs">
  <div class="brand abs"><span class="brand-dot"></span><span class="brand-name">Corvel Imaging Center</span></div>
  <div class="top-contact abs">(954) 555-0142 &nbsp;|&nbsp; info@corvelimaging.example</div>
  <nav class="main-nav abs"><span>HOME</span><span>ABOUT US</span><span>SCANS WE OFFER</span><span>PATIENT AREA</span><span>TYPES OF SCANS</span><span>REFERRALS</span><span>INSURANCE</span><span>CONTACT</span></nav>
</header>

<section class="hero abs">
  <svg class="abs" width="1200" height="470" style="left:0;top:0">
    <polygon points="0,300 420,470 0,470" fill="#c8e6a0" opacity=".7"/>
    <polygon points="860,0 1200,0 1200,260" fill="#c8e6a0" opacity=".6"/>
    <polygon points="0,0 260,0 0,180" fill="#e2f2d0"/>
  </svg>
  <div class="hero-ring abs"></div>
  <div class="photo hero-photo" role="img" aria-label="Smiling female doctor with stethoscope"></div>
  <div class="hero-badge abs">
    <h1>MRI Imaging for Breast Cancer</h1>
    <p>Early detection with our 3.0 Tesla MRI gives clear, detailed views and fast results for you and your doctor.</p>
    <span class="btn">Read more</span>
  </div>
</section>

<section class="intro abs">
  <div class="section-title abs" style="left:240px;top:20px"><i></i>Corvel Imaging Center</div>
  <div class="abs" style="left:240px;top:60px;width:200px">
    <p>The Corvel Center is the most advanced free standing diagnostic imaging center in Florida. Our renovated facility offers MRI, PET/CT, bone density and ultrasound scans.</p>
  </div>
  <div class="callout abs" style="left:460px;top:50px;width:150px">
    <h3>Why would you send your patients anywhere else?</h3>
    <p>Fast scheduling, expert readers and reports your office receives the same day.</p>
  </div>
  <div class="photo" style="left:620px;top:50px;width:90px;height:130px" role="img" aria-label="Female doctor portrait"></div>
  <div class="photo" style="left:960px;top:0;width:160px;height:150px" role="img" aria-label="Happy senior male patient"></div>
  <div class="abs" style="left:860px;top:50px;color:var(--green);font-size:20px;font-weight:700">Schedule today</div>
  <div class="schedule-box abs">
    <div class="bar">Please don't hesitate to call us</div>
    <div class="phone">(954) 555-0142</div>
    <p>or email us at info@corvelimaging.example to book your scan.</p>
    <p>Referring physicians can send orders online any time.</p>
    <div class="field-row"><b>MRI GUIDE</b><span>Preparation &amp; what to expect</span></div>
    <div class="field-row"><b>INSURANCE</b><span>Plans we accept</span></div>
  </div>
  <div class="highlights abs">
    <h4>Tralimo offers the most advanced KW diagnostic imaging systems including:</h4>
    <ul><li>KW Orvanta QX420 3.0 Tesla MRI</li><li>128 slice PET/CT scanner</li><li>High resolution Vantro T4 ultrasound</li><li>Bone density scanning</li></ul>
  </div>
  <p class="abs" style="left:240px;top:370px;width:460px">We are open 7 days per week with after-hours appointments. Our staff are the most experienced in the region and our reading radiologists are board certified specialists.</p>
  <p class="abs" style="left:240px;top:420px;width:460px">We accept most insurance plans.</p>
  <div class="section-title abs" style="left:240px;top:455px;font-size:16px"><i></i>TRALIMO</div>
  <p class="abs" style="left:240px;top:485px;width:820px">Why wait until you are sick to find out about a serious health problem? Tralimo offers full body screening using MRI for people who want early answers. Our screening studies are quick, comfortable and reviewed by experienced radiologists who explain every result clearly.</p>
</section>

<section class="blog abs">
  <div class="blog-title abs">Read Our <b>Blog</b></div>
  <div class="photo" style="left:0;top:60px;width:230px;height:330px" role="img" aria-label="Smiling male doctor"></div>
  <div class="photo" style="left:1070px;top:60px;width:130px;height:330px" role="img" aria-label="Female nurse"></div>
  <div class="card" style="left:240px;top:60px"><div class="photo thumb" role="img" aria-label="MRI scanner"></div><div class="body"><h3>KW Orvanta QX420</h3><p>Our 3.0 Tesla MRI delivers sharp images in shorter scan times, with a wide bore that keeps patients at ease during every study.</p></div><span class="btn">More</span></div>
  <div class="card" style="left:660px;top:60px"><div class="photo thumb" role="img" aria-label="PET/CT scanner"></div><div class="body"><h3>KW Orvanta 480</h3><p>The 128 slice PET/CT combines metabolic and anatomic detail in one visit, helping doctors plan care with confidence.</p></div><span class="btn">More</span></div>
  <div class="card" style="left:240px;top:300px"><div class="photo thumb" role="img" aria-label="Ultrasound machine"></div><div class="body"><h3>KW Vantro T4</h3><p>High resolution ultrasound for abdominal, vascular and breast studies, performed by our certified sonographers.</p></div><span class="btn">More</span></div>
  <div class="card" style="left:660px;top:300px"><div class="photo thumb" role="img" aria-label="Happy patients with staff"></div><div class="body"><h3>Happy Patients</h3><p>Read what our patients say about friendly staff, short waits and clear explanations of their scans and results.</p></div><span class="btn">More</span></div>
</section>

<section class="team abs">
  <div class="team-title abs">Our <b>Team</b></div>
  <div class="team-sub abs">Our team of experienced radiologists and friendly staff are here to help you every step of the way.</div>
  <div class="member" style="left:360px"><div class="photo" role="img" aria-label="Male radiologist portrait"></div><div class="name">Dr. Nathan Orel<br>Radiologist</div></div>
  <div class="member" style="left:550px"><div class="photo" role="img" aria-label="Female physician portrait"></div><div class="name">Dr. Mira Solace<br>Medical Director</div></div>
  <div class="member" style="left:740px"><div class="photo" role="img" aria-label="Male physician portrait"></div><div class="name">Dr. Evan Brisk<br>Nuclear Medicine</div></div>
</section>

<section class="contact abs">
  <div class="photo" style="left:240px;top:0;width:190px;height:240px" role="img" aria-label="Smiling female receptionist"></div>
  <div class="contact-info abs">
    <h2>Contact Us</h2>
    <p><b>Corvel Imaging Center</b><br>210 Harbor Vale Rd, Suite 4<br>Fort Lauderdale, FL</p>
    <p>Phone: (954) 555-0142<br>Fax: (954) 555-0143</p>
    <p>info@corvelimaging.example</p>
    <p>Open Mon–Sun<br>7:00 am – 10:00 pm</p>
  </div>
  <div class="social abs"><i></i><i></i><i></i><span>JOIN OUR<br>SOCIAL MEDIA</span></div>
  <div class="questions abs">
    <h2>HAVE ANY <b>QUESTIONS</b></h2>
    <p style="font-size:10px;margin-top:6px">Send us a message and our team will reply within one business day.</p>
    <div class="form">
      <div><label>Name</label><div class="in"></div></div>
      <div style="grid-row:span 3"><label>Message</label><div class="in msg"></div></div>
      <div><label>Email</label><div class="in"></div></div>
      <div><label>Phone</label><div class="in"></div></div>
      <div><span class="btn">Send</span></div>
    </div>
  </div>
  <div class="help abs"><strong>HELP US, HELP YOU</strong><span>Download our patient forms before your visit to save time.</span></div>
  <svg class="abs" width="140" height="420" style="left:1060px;top:0"><polygon points="140,0 140,420 0,420" fill="#c8e6a0"/></svg>
  <div class="photo" style="left:1090px;top:170px;width:110px;height:210px" role="img" aria-label="Female doctor with tablet"></div>
</section>

<footer class="site-footer abs">
  <div class="footer-links abs"><span>Home</span><span>About Us</span><span>Scans We Offer</span><span>Patient Area</span><span>Referrals</span><span>Insurance</span><span>Forms</span><span>Contact</span></div>
  <div class="copy abs">© Corvel Imaging Center. All rights reserved.</div>
</footer>

</body>
</html>
```